音楽ホールや楽器店、コンサートでの挟み込みで目をひくように、明るい色調で楽しい感じが出ると嬉しいです。
チラシは上1/3しか見えない状況も多い(楽器店のチラシ置き場など)ので、タイトルを上にはっきりとお願いいたします。
記載項目
【おもて面】

[タイトル]響きと拍子のふしぎな音楽会
[日時]2017年9月9日(土) 13:30開場 14:00開演
[場所]白浜ゆめまちホール中ホール
北九州市八幡西区杉が丘4-3-7 Tel:093-555-0182
[チケット]全席自由 一般2,000円 高校生以下1,000円 当日500円増
[出演]森田千春・藤野早苗・大場律子・堀江真弓
[プログラム]Nimbuscor/T.R.Bellamy トルヴァ/ヴィルトマイヤー 北極星の庭/L.Ferrucci 他
[チケット販売]チケットすずらん(※現在手続き中)
[お問い合わせ]090-5550-3419(森田)

※カラーの4人写真とタイトルを上部に
※マリンバや打楽器の写真をおもて面のどこかに(もしくは背景に)
※東和マテリアル商事株式会社地域文化支援助成事業と記載

【うら面】
[メッセージ]
打楽器ってどんな楽器?音が大きい?簡単?よくわからない??
そんなあなたに聴いてほしい、見てほしい。
さあ、ふしぎな音楽会の始まりです。
生演奏が織りなすスリル。鼓動が生み出すリズム。
空気の振動に身をゆだねてみてください。
ちょっとカッコよくて、ちょっと面白くて、かなり楽しい・・・
そんな打楽器の魅力にあなたもマニアになっちゃうかも。きっとね♪

※補足に続きます
A4
両面
赤系、水色系、緑系、黄・オレンジ系
※チラシ記載内容の続き

[写真&プロフィール]
白黒横並びの4人写真をウラ面中段あたりに。
写真の下を4ブロックに分け、各々のプロフィール文。※添付ファイル参照
左から
(堀江真弓)(大場律子)(藤野早苗)(森田千春)

※写真や文字の配列はイメージです。かならずしもその通りでなくても構いません。
よろしくお願いいたします。
■ 選んだ理由

ぱっと目を惹くカラーとデザインで、明るく楽しい感じがメンバー内で人気だったため、今回お願いすることになりました。

■ 提案者全員のお礼・コメント

沢山のご提案、ありがとうございました。
奏者4人で話し合ったのですが、素敵なデザインだらけで意見が割れ、決定まで時間がかかりました。
最終的には、“マニアックなコンサートだからこそ敷居を感じて欲しくない”ということを主軸に置いた結果、今回の方にお願いすることになりました。

気になるご提案が多すぎて、いくつもチラシを作りたい気持ちになるほどでした。
この場をお借りして、ご提案くださった方全員にお礼申し上げます。
本当にありがとうございました。

```html
<!DOCTYPE html>
<html lang="ja">
<head>
<meta charset="utf-8">
<title>響きと拍子のふしぎな音楽会</title>
<link href="https://fonts.googleapis.com/css2?family=M+PLUS+Rounded+1c:wght@400;700;800&family=Noto+Sans+JP:wght@400;500;700&family=Dancing+Script:wght@600&display=swap" rel="stylesheet">
<style>
:root{
  --wine:#8c2232;
  --wine-dark:#6e1826;
  --wine-text:#a3283b;
  --pink:#f6d3d9;
  --cream:#fbf4ec;
  --white:#ffffff;
  --gold:#f3e2c4;
}
*{margin:0;padding:0;box-sizing:border-box}
html,body{width:849px;height:1200px;overflow:hidden;background:#eee}
.flyer{position:relative;width:849px;height:1200px;overflow:hidden;background:var(--cream);font-family:"Noto Sans JP",sans-serif;color:var(--wine-text)}
.hero{position:absolute;left:0;top:0;width:849px;height:838px;background:linear-gradient(180deg,var(--wine) 0%,#992a3b 55%,var(--wine-dark) 100%)}
.hero__subtitle{position:absolute;top:50px;width:100%;text-align:center;font-family:"M PLUS Rounded 1c",sans-serif;font-weight:700;font-size:36px;color:var(--white);letter-spacing:4px}
.hero__script{position:absolute;top:96px;width:100%;text-align:center;font-family:"Dancing Script",cursive;font-size:22px;color:var(--gold)}
.hero__title{position:absolute;top:118px;width:100%;text-align:center;font-family:"M PLUS Rounded 1c",sans-serif;font-weight:800;font-size:100px;line-height:1;color:var(--white);letter-spacing:6px}
.hero__tagline{position:absolute;top:228px;width:100%;text-align:center;font-family:"Dancing Script",cursive;font-size:20px;color:var(--gold);letter-spacing:1px}
.members-photo{position:absolute;left:92px;top:250px;width:362px;height:560px;border-radius:6px;background:linear-gradient(160deg,#c98a7a 0%,#e7b9a8 35%,#3f6d8c 70%,#7d3b4c 100%)}
.event-date{position:absolute;left:470px;top:262px;font-family:"M PLUS Rounded 1c",sans-serif;font-weight:800;color:var(--pink);font-size:34px;white-space:nowrap}
.event-date b{font-size:60px}
.event-date small{font-size:26px}
.event-time{position:absolute;left:520px;top:345px;display:flex;gap:10px;align-items:center;font-size:17px;color:var(--white)}
.event-time span.tag{background:var(--white);color:var(--wine);padding:1px 6px;font-size:13px;font-weight:700}
.venue{position:absolute;left:478px;top:380px;color:var(--white)}
.venue__name{font-family:"M PLUS Rounded 1c",sans-serif;font-weight:700;font-size:28px;white-space:nowrap}
.venue__name small{font-size:22px}
.venue__address{font-size:15px;margin-top:4px;display:flex;gap:14px;align-items:center}
.venue__address svg{vertical-align:-3px}
.instrument-photos{position:absolute;left:466px;top:448px;width:344px;height:340px;display:grid;grid-template-columns:1fr 1fr;grid-template-rows:1fr 1fr;gap:6px}
.instrument-photos div{border-radius:3px}
.tile-marimba{background:linear-gradient(135deg,#5a3220,#b97a4c,#3b2418)}
.tile-wood{background:linear-gradient(135deg,#d9c3a0,#8f6a44)}
.tile-drum{background:linear-gradient(135deg,#2b2b2f,#9c9aa0,#4a3a32)}
.tile-timpani{background:linear-gradient(135deg,#b07a3e,#e2b77a,#6b4426)}
.lineup{position:absolute;top:852px;width:100%;text-align:center}
.label{display:inline-block;font-size:15px;color:var(--wine-text);letter-spacing:2px}
.lineup__names{font-family:"M PLUS Rounded 1c",sans-serif;font-weight:700;font-size:30px;letter-spacing:2px;margin-top:2px}
.program{position:absolute;top:928px;width:100%;text-align:center}
.program__list{margin:6px auto 0;width:480px;font-size:19px;font-weight:500;color:#5a3a3a}
.program__list li{list-style:none;display:flex;justify-content:space-between;line-height:32px}
.program__list .etc{margin-left:10px}
.tickets{position:absolute;top:1062px;width:100%;text-align:center}
.tickets__bar{display:inline-block;width:440px;background:var(--wine);color:var(--white);font-size:16px;letter-spacing:3px;padding:2px 0;border-radius:3px}
.tickets__prices{font-family:"M PLUS Rounded 1c",sans-serif;font-weight:700;font-size:22px;margin-top:6px}
.tickets__prices b{font-size:34px}
.tickets__sale{font-size:15px;margin-top:2px;display:flex;justify-content:center;gap:40px;color:#5a3a3a}
.sponsor{position:absolute;bottom:14px;width:100%;text-align:center;font-size:13px;color:#5a3a3a;letter-spacing:1px}
</style>
</head>
<body>
<div class="flyer">
  <section class="hero">
    <p class="hero__subtitle">響きと拍子の</p>
    <p class="hero__script">Marimba &amp; Percussion</p>
    <h1 class="hero__title">ふしぎな音楽会</h1>
    <p class="hero__tagline">Enthusiastic concert</p>
    <div class="members-photo" role="img" aria-label="出演者4人のカラー写真"></div>
    <p class="event-date"><b>2017</b>年<b>9</b>月<b>9</b>日<small>(土)</small></p>
    <p class="event-time"><span class="tag">開場</span>13:30 <span class="tag">開演</span>14:00</p>
    <div class="venue">
      <p class="venue__name">白浜ゆめまちホール <small>中ホール</small></p>
      <p class="venue__address">北九州市八幡西区杉が丘4-3-7
        <span><svg width="16" height="16" viewBox="0 0 24 24" fill="#fff"><path d="M6.6 10.8a15 15 0 0 0 6.6 6.6l2.2-2.2a1 1 0 0 1 1-.25 11 11 0 0 0 3.6.57 1 1 0 0 1 1 1V20a1 1 0 0 1-1 1A17 17 0 0 1 3 4a1 1 0 0 1 1-1h3.5a1 1 0 0 1 1 1c0 1.25.2 2.45.57 3.57a1 1 0 0 1-.25 1z"/></svg> 093-555-0182</span></p>
    </div>
    <div class="instrument-photos">
      <div class="tile-marimba" role="img" aria-label="マリンバの写真"></div>
      <div class="tile-wood" role="img" aria-label="木製打楽器の写真"></div>
      <div class="tile-timpani" role="img" aria-label="ティンパニの写真"></div>
      <div class="tile-drum" role="img" aria-label="ドラムの写真"></div>
    </div>
  </section>

  <section class="lineup">
    <span class="label">出演</span>
    <p class="lineup__names">森田千春・藤野早苗・大場律子・堀江真弓</p>
  </section>

  <section class="program">
    <span class="label">プログラム</span>
    <ul class="program__list">
      <li><span>『Nimbuscor』</span><span>T.R.Bellamy</span></li>
      <li><span>『トルヴァ』</span><span>ヴィルトマイヤー</span></li>
      <li><span>『北極星の庭』</span><span>L.Ferrucci<span class="etc">他</span></span></li>
    </ul>
  </section>

  <section class="tickets">
    <span class="tickets__bar">チケット　全席自由</span>
    <p class="tickets__prices">一般 <b>2,000</b>円　高校生以下 <b>1,000</b>円 <small>(当日+500円)</small></p>
    <p class="tickets__sale"><span>[チケット販売] チケットすずらん</span><span>(お問い合わせ) 090-5550-3419(森田)</span></p>
  </section>

  <p class="sponsor">東和マテリアル商事株式会社地域文化支援助成事業</p>
</div>
</body>
</html>
```